Rocket business card

Modern business card design, use of color is good with clean space too.

Things to include on card:

Quote: I add fuel to your optometry practice

- Eyewear Sales
- Admin Duties
- Revenue Collection
- Leadership
- Tech Adoption
- COGS Reduction
- Product Sourcing
-Medical Growth

Dalton Vessey, CEO
Glint Harbor
Text Me! 847-302-1964
dalton@glintharbor.example

```html
<!DOCTYPE html>
<html lang="en">
<head>
<meta charset="utf-8">
<title>Glint Harbor – Business Card</title>
<link rel="stylesheet" href="https://fonts.googleapis.com/css2?family=Montserrat:wght@400;500;700&display=swap">
<style>
  :root {
    --backdrop: #2a2a2a;
    --card: #0b0b0b;
    --ink: #ffffff;
    --amber: #f7a11a;
    --ember: #e4412a;
    --muted: #d9d9d9;
  }
  * { box-sizing: border-box; margin: 0; padding: 0; }
  html, body {
    width: 1200px; height: 900px; overflow: hidden;
    background: var(--backdrop);
    font-family: "Montserrat", Arial, sans-serif;
    color: var(--ink);
  }
  .canvas {
    position: relative; width: 1200px; height: 900px;
    display: flex; flex-direction: column; align-items: center; justify-content: center; gap: 40px;
  }
  .card {
    position: relative; width: 660px; height: 380px;
    background: var(--card);
    box-shadow: 0 18px 40px rgba(0,0,0,.55);
  }
  .brand {
    position: absolute; display: flex; align-items: center; gap: 14px;
    font-weight: 500; letter-spacing: .04em; color: var(--ink);
  }
  .brand-dot {
    border-radius: 50%;
    background: linear-gradient(135deg, var(--ember), var(--amber));
  }
  /* back */
  .card-back .brand { left: 120px; top: 80px; font-size: 30px; }
  .card-back .brand-dot { width: 36px; height: 36px; }
  .services { position: absolute; list-style: none; font-size: 17px; line-height: 22px; letter-spacing: .04em; color: var(--muted); }
  .services li { display: flex; align-items: center; gap: 10px; }
  .services li::before { content: ""; width: 6px; height: 6px; border-radius: 50%; background: var(--ink); }
  .services-left { left: 120px; top: 200px; }
  .services-right { right: 70px; top: 270px; text-align: right; }
  .services-right li { flex-direction: row-reverse; }
  /* front */
  .card-front .brand { left: 50px; top: 70px; font-size: 36px; }
  .card-front .brand-dot { width: 44px; height: 44px; }
  .divider {
    position: absolute; left: 50px; right: 50px; top: 215px; height: 2px;
    background: linear-gradient(90deg, var(--ember), var(--amber));
  }
  .identity { position: absolute; right: 55px; top: 170px; font-size: 25px; letter-spacing: .04em; }
  .identity .name { color: var(--amber); font-weight: 700; text-transform: uppercase; }
  .identity .role { font-weight: 400; font-size: 22px; }
  .contact { position: absolute; right: 55px; top: 238px; font-size: 18px; line-height: 26px; text-align: right; letter-spacing: .02em; }
  .contact p { display: flex; align-items: center; justify-content: flex-end; gap: 8px; }
  .contact .cue { color: var(--amber); }
  .contact svg { width: 18px; height: 18px; }
  .tagline {
    position: absolute; right: 55px; top: 305px; text-align: right;
    font-size: 20px; line-height: 26px; letter-spacing: .1em; text-transform: uppercase;
  }
</style>
</head>
<body>
<main class="canvas">
  <section class="card card-back">
    <div class="brand"><span class="brand-dot"></span>Glint Harbor</div>
    <ul class="services services-left">
      <li>Eyewear Sales</li>
      <li>Admin Duties</li>
      <li>Revenue Collection</li>
      <li>Leadership</li>
    </ul>
    <ul class="services services-right">
      <li>Tech Adoption</li>
      <li>COGS Reduction</li>
      <li>Product Sourcing</li>
      <li>Medical Growth</li>
    </ul>
  </section>

  <section class="card card-front">
    <div class="brand"><span class="brand-dot"></span>Glint Harbor</div>
    <div class="divider"></div>
    <p class="identity"><span class="name">Dalton Vessey</span> <span class="role">| CEO</span></p>
    <div class="contact">
      <p>
        <svg viewBox="0 0 24 24" fill="none" stroke="#e4412a" stroke-width="2"><circle cx="12" cy="12" r="9"/><path d="M9 8l2 2-1 1.5 2.5 2.5L14 13l2 2-1.5 1.5C11 16 8 13 7.5 9.5z"/></svg>
        <span class="cue">Text Me!</span> 847-302-1964
      </p>
      <p>
        <svg viewBox="0 0 24 24" fill="none" stroke="#e4412a" stroke-width="2"><rect x="3" y="6" width="18" height="12"/><path d="M3 6l9 7 9-7"/></svg>
        dalton@glintharbor.example
      </p>
    </div>
    <p class="tagline">I add fuel to your<br>optometry practice</p>
  </section>
</main>
</body>
</html>
```